Business Card Design for Marketing Firm

Looking for business card design for higher end marketing firm. Clean but impressionable/trendy. We are a marketing firm that represents manufacturers in the foodservice equipment and supply industry. Our customers are end users such has hotels, restaurants, country clubs, convention centers and casinos as well as distributors of restaurants supplies and equipment, and manufacturers of foodservice equipment and supplies.
Target Market(s)
Hotels, Restaurants, Supply & Equipment Distributors, Foodservice Manufacturers
Industry/Entity Type
Foodservice/Hospitality
Contact Information for Business Card
Name, Title, Contact Number, Email, Website, Social Media, Address
Requirements
Must have
- Clean & Simple but Serious and Impressionable

```html
<!DOCTYPE html>
<html lang="en">
<head>
<meta charset="utf-8">
<title>Meridian Service Partners – Business Card</title>
<link rel="stylesheet" href="https://fonts.googleapis.com/css2?family=Cinzel:wght@400;600&family=EB+Garamond:wght@400;500&display=swap">
<style>
  :root {
    --navy: #23246e;
    --navy-line: #2b2d7c;
    --paper: #ffffff;
    --paper-shade: #f1f1f3;
    --ink-grey: #5a5a62;
    --backdrop: #e7e5e1;
    --white: #ffffff;
  }
  * { box-sizing: border-box; margin: 0; padding: 0; }
  html, body {
    width: 1200px; height: 900px; overflow: hidden;
    background: var(--backdrop);
  }
  .sheet {
    width: 1200px; height: 900px;
    display: flex; flex-direction: column; align-items: center; justify-content: center;
    gap: 44px;
  }
  .card {
    width: 640px; height: 366px;
    border-radius: 30px;
    position: relative;
    box-shadow: 0 10px 28px rgba(0,0,0,.14);
    overflow: hidden;
  }

  /* Front */
  .card--front { background: var(--navy); color: var(--white); }
  .brand {
    position: absolute; left: 50%; transform: translateX(-50%);
    display: flex; flex-direction: column; align-items: stretch;
    font-family: "Cinzel", serif; font-weight: 600;
    white-space: nowrap;
  }
  .brand__name { font-size: 27px; letter-spacing: 1px; line-height: 1; }
  .brand__tag { font-size: 15px; letter-spacing: 1px; text-align: right; line-height: 1; margin-top: 2px; }
  .brand__rule { height: 1.5px; background: currentColor; margin-top: 5px; width: 88%; }
  .card--front .brand { top: 130px; }
  .social {
    position: absolute; left: 50%; top: 218px; transform: translateX(-50%);
    display: flex; gap: 12px;
  }
  .social__dot { width: 24px; height: 24px; border-radius: 50%; background: var(--white); }

  /* Back */
  .card--back { background: linear-gradient(120deg, var(--paper-shade), var(--paper) 55%); color: var(--navy); }
  .card--back .brand { top: 62px; left: 47%; }
  .person {
    position: absolute; left: 50%; top: 170px; transform: translateX(-50%);
    text-align: center; white-space: nowrap;
  }
  .person__name { font-family: "Cinzel", serif; font-weight: 600; font-size: 22px; letter-spacing: .5px; }
  .person__title { font-family: "EB Garamond", serif; font-size: 17px; color: var(--ink-grey); margin-top: -2px; }
  .divider {
    position: absolute; left: 40px; right: 40px; top: 258px;
    height: 1.5px; background: var(--navy-line);
  }
  .contact {
    position: absolute; top: 272px;
    font-family: "EB Garamond", serif; font-size: 17px; color: var(--ink-grey);
    display: flex; flex-direction: column; gap: 4px;
  }
  .contact--left { left: 40px; }
  .contact--right { right: 40px; align-items: flex-end; }
  .contact__item { display: flex; align-items: center; gap: 8px; }
  .contact__icon { width: 14px; height: 14px; fill: var(--navy); flex: none; }
</style>
</head>
<body>
<main class="sheet">
  <section class="card card--front" aria-label="Business card front">
    <div class="brand">
      <span class="brand__name">Meridian Service</span>
      <span class="brand__tag">Partners</span>
      <span class="brand__rule"></span>
    </div>
    <div class="social" aria-label="Social media links">
      <span class="social__dot"></span>
      <span class="social__dot"></span>
      <span class="social__dot"></span>
    </div>
  </section>

  <section class="card card--back" aria-label="Business card back">
    <div class="brand">
      <span class="brand__name">Meridian Service</span>
      <span class="brand__tag">Partners</span>
      <span class="brand__rule"></span>
    </div>
    <div class="person">
      <p class="person__name">DANIEL REYES</p>
      <p class="person__title">Director</p>
    </div>
    <div class="divider"></div>
    <div class="contact contact--left">
      <p class="contact__item">
        <svg class="contact__icon" viewBox="0 0 24 24" aria-hidden="true"><path d="M6.6 10.8a15 15 0 0 0 6.6 6.6l2.2-2.2c.3-.3.7-.4 1-.2 1.1.4 2.3.6 3.6.6.6 0 1 .4 1 1V20c0 .6-.4 1-1 1A17 17 0 0 1 3 4c0-.6.4-1 1-1h3.5c.6 0 1 .4 1 1 0 1.3.2 2.5.6 3.6.1.3 0 .7-.2 1z"/></svg>
        555-0142-7788
      </p>
      <p class="contact__item">
        <svg class="contact__icon" viewBox="0 0 24 24" aria-hidden="true"><path d="M12 2a7 7 0 0 0-7 7c0 5.2 7 13 7 13s7-7.8 7-13a7 7 0 0 0-7-7zm0 9.5A2.5 2.5 0 1 1 12 6.5a2.5 2.5 0 0 1 0 5z"/></svg>
        Riverton, Ohio
      </p>
    </div>
    <div class="contact contact--right">
      <p class="contact__item">
        info@meridianservicepartners.com
        <svg class="contact__icon" viewBox="0 0 24 24" aria-hidden="true"><path d="M2 5h20v14H2z M3 6l9 7 9-7" fill="var(--navy)"/><path d="M3 6.5l9 7 9-7" fill="none" stroke="#fff" stroke-width="1.6"/></svg>
      </p>
      <p class="contact__item">
        www.meridianservicepartners.com
        <svg class="contact__icon" viewBox="0 0 24 24" aria-hidden="true"><circle cx="12" cy="12" r="10"/><path d="M2 12h20M12 2c3 3 3 17 0 20M12 2c-3 3-3 17 0 20M4 7h16M4 17h16" fill="none" stroke="#fff" stroke-width="1.3"/></svg>
      </p>
    </div>
  </section>
</main>
</body>
</html>
```